" Apoio para empresas que desejam vender produtos e/ou serviços para órgãos públicos ou empresas que utilizam processos licitatórios em suas compras "

```html
<!DOCTYPE html>
<html lang="pt-BR">
<head>
<meta charset="utf-8">
<title>Pregão Certo — Pasta institucional</title>
<link rel="stylesheet" href="https://fonts.googleapis.com/css2?family=Montserrat:wght@400;500;600;700&display=swap">
<style>
  :root {
    --navy: #141d47;
    --teal: #2a9d93;
    --teal-light: #3db5a9;
    --paper: #ffffff;
    --ghost: #ececec;
    --ink: #3a3f55;
    --stage: #eef0f2;
  }
  * { box-sizing: border-box; margin: 0; padding: 0; }
  html, body {
    width: 1200px; height: 1200px; overflow: hidden;
    background: var(--stage);
    font-family: "Montserrat", sans-serif;
  }
  .folder {
    position: absolute; left: 60px; top: 230px;
    width: 1080px; height: 740px;
    display: flex; flex-direction: column;
    box-shadow: 0 10px 30px rgba(0,0,0,0.12);
  }
  .folder-spread { flex: 1; display: flex; }
  .folder-base { height: 22px; background: var(--teal); }
  .panel { position: relative; width: 50%; height: 100%; overflow: hidden; }
  .panel--inside { background: var(--paper); }
  .panel--cover { background: var(--navy); display: flex; align-items: center; justify-content: center; }

  .brand { display: flex; align-items: center; gap: 14px; }
  .brand-mark { background: var(--teal); flex: none; }
  .brand-text { display: flex; flex-direction: column; }
  .brand-name { font-weight: 600; letter-spacing: 0.02em; line-height: 1; }
  .brand-tagline { font-weight: 500; letter-spacing: 0.12em; text-transform: uppercase; margin-top: 6px; }

  .brand--small { position: absolute; top: 52px; left: 50%; transform: translateX(-50%); }
  .brand--small .brand-mark { width: 34px; height: 34px; }
  .brand--small .brand-name { font-size: 30px; color: var(--navy); }
  .brand--small .brand-tagline { font-size: 10px; color: var(--ink); }

  .brand--large .brand-mark { width: 60px; height: 60px; }
  .brand--large .brand-name { font-size: 52px; color: var(--paper); }
  .brand--large .brand-tagline { font-size: 15px; color: var(--teal-light); margin-top: 10px; }

  .ghost-circle {
    position: absolute; left: -70px; top: 230px;
    width: 380px; height: 380px; border-radius: 50%;
    background: var(--ghost);
  }

  .contact {
    position: absolute; left: 26px; right: 20px; bottom: 26px;
    display: flex; justify-content: space-between;
    font-size: 10px; color: var(--ink); line-height: 1.6;
  }
  .contact-item { display: flex; align-items: flex-start; gap: 5px; }
  .contact-icon { width: 10px; height: 10px; flex: none; margin-top: 2px; fill: var(--teal); }
</style>
</head>
<body>
  <div class="folder">
    <div class="folder-spread">
      <section class="panel panel--inside">
        <div class="brand brand--small">
          <span class="brand-mark"></span>
          <div class="brand-text">
            <span class="brand-name">Pregão Certo</span>
            <span class="brand-tagline">Soluções em Licitações</span>
          </div>
        </div>
        <div class="ghost-circle"></div>
        <div class="contact">
          <div class="contact-col">
            <div class="contact-item">
              <svg class="contact-icon" viewBox="0 0 10 10"><path d="M2 0.5 L3.8 0.5 L4.3 3 L3 3.8 Q4 6 6.2 7 L7 5.7 L9.5 6.2 L9.5 8 Q9.5 9.5 8 9.5 Q0.5 9 0.5 2 Q0.5 0.5 2 0.5Z"/></svg>
              <span>(11) 4000-1234 · (11) 99000-1234</span>
            </div>
            <div class="contact-item">
              <svg class="contact-icon" viewBox="0 0 10 10"><rect x="0.5" y="2" width="9" height="6.5" rx="1"/></svg>
              <span>contato@pregaocerto.com.br</span>
            </div>
          </div>
          <div class="contact-item">
            <svg class="contact-icon" viewBox="0 0 10 10"><path d="M5 0.3 A3.5 3.5 0 0 1 8.5 3.8 C8.5 6.5 5 9.7 5 9.7 C5 9.7 1.5 6.5 1.5 3.8 A3.5 3.5 0 0 1 5 0.3Z"/></svg>
            <span>Av. das Palmeiras, 125 - 8º Andar<br>Torre Norte - Centro - SP 01000-000</span>
          </div>
        </div>
      </section>
      <section class="panel panel--cover">
        <div class="brand brand--large">
          <span class="brand-mark"></span>
          <div class="brand-text">
            <span class="brand-name">Pregão Certo</span>
            <span class="brand-tagline">Soluções em Licitações</span>
          </div>
        </div>
      </section>
    </div>
    <div class="folder-base"></div>
  </div>
</body>
</html>
```